Industrial Company Profile Brochure Design

We need company profile brochure design. We are in industrial valve business and we are serving oil, petrochemical and power plants. We are working with our clients as trusted advisor. So, the final design should communicate valve solutions expert. The brochure should be 4 pages (including front and back) or folded style. However, it is open. We do not like to put any restriction on creativity. We leave the decision for number of pages and page size to the designer. The color theme should be same as / compatible with logo colors. You should use icons.Find attached the followings:- Our Logo- Word file that contains the required content (text and photos) for the brochure.3 Modern brochure designs. We like these designs. This is just to give you idea about what we like. The brochure is simple, clear and easy to get full information quickly.- Just banner for valve and components. You may need it.

Target Market(s)

The end users of oi, petrochemical and power plants

Industry/Entity Type

Engineering Consulting

Requirements
Must have
• - You must add our slogan. It is "Your Valves Solutions Expert"

```html
<!DOCTYPE html>
<html lang="en">
<head>
<meta charset="utf-8">
<title>Raslan Valveworks – Company Profile Brochure</title>
<link href="https://fonts.googleapis.com/css2?family=Arimo:wght@400;700&display=swap" rel="stylesheet">
<style>
  :root {
    --orange: #F7981F;
    --grey: #828185;
    --grey-dark: #6E6D71;
    --white: #FFFFFF;
    --ink: #111111;
    --text-grey: #7B7A7E;
  }
  * { margin: 0; padding: 0; box-sizing: border-box; }
  html, body { width: 1200px; height: 1000px; overflow: hidden; background: var(--white); }
  body { font-family: "Arimo", Arial, sans-serif; }
  .sheet {
    position: absolute; left: 0; top: 0;
    width: 2100px; height: 1760px;
    transform: scale(0.568); transform-origin: 0 0;
  }
  .abs { position: absolute; }
  .panel { position: absolute; overflow: hidden; }
  .spread-frame { position: absolute; border: 1.5px solid #222; pointer-events: none; }
  .fill-orange { background: var(--orange); }
  .fill-grey { background: var(--grey); }
  .fill-white { background: var(--white); }

  .title { position: absolute; font-weight: 400; color: var(--white); font-size: 26px; line-height: 1; }
  .body-text { position: absolute; font-size: 10.2px; line-height: 12.7px; color: var(--white); text-align: justify; }
  .body-text p + p { margin-top: 12.7px; }
  .on-white { color: var(--ink); }

  .photo { position: absolute; }

  .adv-list { position: absolute; left: 0; width: 276px; height: 170px; background: var(--grey); list-style: none; padding-top: 4px; }
  .adv-list li { height: 24.3px; border-bottom: 2px solid var(--white); color: var(--white); font-size: 10.2px; line-height: 24px; padding-left: 58px; }
  .adv-list li:last-child { border-bottom: none; }

  .bullets { list-style: none; }
  .bullets li { position: relative; padding-left: 29px; }
  .bullets li::before { content: "•"; position: absolute; left: 0; }

  .why-title { font-size: 38px; color: var(--ink); }
  .why-head { font-size: 25px; color: var(--white); }

  .contact { position: absolute; font-size: 10.2px; line-height: 14.6px; color: var(--white); font-style: normal; }

  .brand-mark { position: absolute; display: flex; flex-direction: column; align-items: center; }
  .brand-mark .dot { width: 58px; height: 58px; border-radius: 50%; background: var(--orange); margin-bottom: 14px; }
  .brand-mark .name { font-weight: 700; font-size: 25px; line-height: 28px; color: var(--orange); text-align: center; }
  .slogan { position: absolute; font-size: 21px; color: var(--grey-dark); transform: rotate(-90deg); transform-origin: 0 0; white-space: nowrap; }

  .section-head { position: absolute; font-size: 25px; font-weight: 400; color: var(--text-grey); line-height: 1; }
  .head-bar { position: absolute; height: 11px; background: var(--orange); }

  .page-label { position: absolute; font-size: 24px; color: var(--ink); }
</style>
</head>
<body>
<div class="sheet">

  <!-- Upgrade & Retrofit -->
  <section class="panel fill-white" style="left:82px; top:118px; width:483px; height:682px;">
    <div class="abs fill-orange" style="left:0; top:0; width:483px; height:139px;"></div>
    <div class="abs fill-orange" style="left:276px; top:139px; width:207px; height:170px;"></div>
    <h2 class="title" style="left:58px; top:71px;">Upgrade &amp; Retrofit</h2>
    <p class="body-text" style="left:58px; top:107px; width:368px; text-align:left;">We supply highly reliable and efficient upgrading solutions for our clients, with the following key advantages:</p>
    <ul class="adv-list" style="top:139px;">
      <li>Fits well into the existing valve</li>
      <li>Full responsibility of the valve</li>
      <li>Detailed documentation</li>
      <li>Saves the cost of piping modifications</li>
      <li>Lower installation costs</li>
      <li>Shorter plant downtime</li>
    </ul>
    <div class="photo" role="img" aria-label="Yellow and white valve positioner unit on a mounting column" style="left:296px; top:152px; width:118px; height:276px; background:linear-gradient(90deg,#C9A21E 0%,#E7C52F 40%,#E9E9EA 60%,#D6D6D8 100%);"></div>
    <div class="photo" role="img" aria-label="Compressor capacity control actuator" style="left:98px; top:355px; width:172px; height:135px; background:linear-gradient(160deg,#E3E4E6,#A9ABAF);"></div>
    <div class="abs" role="img" aria-label="Partner badge" style="left:62px; top:330px; width:52px; height:14px; background:#2A4D8F;"></div>
    <div class="abs" role="img" aria-label="Partner badge" style="left:260px; top:478px; width:32px; height:11px; background:#D8A7A7;"></div>
    <div class="photo" role="img" aria-label="Technical drawing of valve unloader" style="left:62px; top:518px; width:68px; height:84px; background:#F1F1F1;"></div>
    <div class="photo" role="img" aria-label="Technical drawing of valve cross section" style="left:148px; top:518px; width:74px; height:84px; background:#EDEDED;"></div>
    <div class="photo" role="img" aria-label="Compressor valve plate drawing, black" style="left:238px; top:518px; width:86px; height:84px; background:linear-gradient(135deg,#5A5A5A,#2E2E2E);"></div>
    <div class="photo" role="img" aria-label="Compressor valve plate drawing, green" style="left:334px; top:518px; width:88px; height:84px; background:linear-gradient(135deg,#6DBE78,#3FA34D);"></div>
    <div class="abs fill-orange" style="left:0; top:652px; width:483px; height:30px;"></div>
  </section>

  <!-- Spare Parts -->
  <section class="panel fill-grey" style="left:565px; top:118px; width:482px; height:682px;">
    <h2 class="title" style="left:57px; top:71px;">Spare Parts</h2>
    <div class="body-text" style="left:57px; top:107px; width:368px;">
      <p>We are not only focus on providing reliable valves and upgrades, but also assist our clients in maintaining their valves. We provide direct OEM part replacements, with quality same as those originally installed. Other than providing common spare parts, we can also help in the replacement of obsolete parts not commonly available by using our trusted sources or our highly advanced reverse engineering techniques.</p>
      <div style="text-align:left;">The advantages of using spare parts provided by us are as follows:</div>
      <ul class="bullets" style="text-align:left;">
        <li>Completely interchangeable</li>
        <li>Use of latest technology makes our parts highly reliable</li>
        <li>Lower costs</li>
        <li>Faster delivery</li>
      </ul>
    </div>
    <div class="photo" role="img" aria-label="Assorted O-rings and seals in orange, black and white" style="left:0; top:257px; width:320px; height:100px; background:linear-gradient(90deg,#E58C1C,#3B2A1A 45%,#D98418 70%,#2B2520);"></div>
    <div class="photo" role="img" aria-label="Machined valve cage component" style="left:320px; top:257px; width:105px; height:100px; background:linear-gradient(135deg,#8C8A84,#C9C6BE 50%,#6F6C66);"></div>
    <div class="photo" role="img" aria-label="Perforated valve plug and stem on a workbench" style="left:95px; top:357px; width:197px; height:130px; background:linear-gradient(135deg,#4A4844,#9C988F 50%,#5A5650);"></div>
    <div class="photo" role="img" aria-label="Polished stainless valve trim parts" style="left:292px; top:357px; width:190px; height:130px; background:linear-gradient(135deg,#B6B5B2,#6D6C69 55%,#C4C3C0);"></div>
    <div class="abs fill-white" style="left:0; top:487px; width:482px; height:165px;"></div>
    <div class="photo" role="img" aria-label="Spiral wound gasket cut-away photo" style="left:57px; top:500px; width:358px; height:124px; background:linear-gradient(180deg,#F4F4F5,#C9CACD);"></div>
  </section>

  <!-- Why Us -->
  <section class="panel fill-orange" style="left:1047px; top:118px; width:481px; height:682px;">
    <h2 class="title why-title" style="left:76px; top:74px;">Why Us</h2>
    <h3 class="title why-head" style="left:76px; top:144px;">Quality Control</h3>
    <p class="body-text" style="left:76px; top:180px; width:276px;">Our quality control processes, implemented across all stages of valve solutions development, help in keeping our solutions highly reliable and accurate for long-term implementations.</p>
    <h3 class="title why-head" style="left:76px; top:249px;">Customer Satisfaction</h3>
    <p class="body-text" style="left:76px; top:285px; width:276px;">Our teams are committed to handling the needs of our customers in a timely manner, keeping them satisfied and happy. This also makes us a reliable choice for any kind of upgrade or replacement parts in an emergency situation.</p>
    <h3 class="title why-head" style="left:76px; top:354px;">Highly Affordable</h3>
    <p class="body-text" style="left:76px; top:390px; width:276px;">Our awareness of the latest technologies and unique methods assists us in providing solutions with lower costs; we make sure to pass on this advantage to our clients by keeping our services highly affordable for them.</p>
    <div class="abs fill-grey" style="left:0; top:472px; width:481px; height:210px;"></div>
    <address class="contact" style="left:223px; top:556px;">
      Contact Details:<br>
      Raslan Valveworks | M +966512340987<br>
      Harbour Rd - Dammam &nbsp;| 31100 | KSA<br>
      info@raslan.example | www.raslan.example
    </address>
  </section>

  <!-- Front cover -->
  <section class="panel" style="left:1528px; top:118px; width:482px; height:682px; background:linear-gradient(90deg,#EDEDED,#FFFFFF 70%,#E9E9E9);">
    <div class="photo" role="img" aria-label="Control valve with red pneumatic actuator and dark grey body" style="left:0; top:0; width:482px; height:682px; background:linear-gradient(180deg,#C8472A 0%,#D25A34 30%,#9A9C9E 42%,#5C6466 60%,#4E5658 100%); clip-path:polygon(0 0,54% 0,54% 84%,100% 70%,100% 100%,0 100%);"></div>
    <div class="brand-mark" style="left:285px; top:42px; width:166px;">
      <span class="dot"></span>
      <span class="name">RASLAN<br>Valveworks</span>
    </div>
    <p class="slogan" style="left:262px; top:522px;">"Your Valves Solutions Expert"</p>
  </section>

  <div class="spread-frame" style="left:82px; top:118px; width:965px; height:682px;"></div>

  <span class="page-label" style="left:1456px; top:810px;">Back</span>
  <span class="page-label" style="left:1945px; top:810px;">Front</span>

  <!-- Inner 1 -->
  <section class="panel fill-white" style="left:82px; top:900px; width:483px; height:682px;">
    <div class="abs fill-orange" style="left:0; top:58px; width:483px; height:252px;"></div>
    <h2 class="title" style="left:58px; top:71px;">About Us</h2>
    <div class="body-text" style="left:58px; top:106px; width:368px;">
      <p>Raslan Valveworks was established to provide highly-reliable consultation services for a selection of valve designs for various industrial applications. We specialize in recommending new valves for different types of industrial needs, as well as re-engineering the obsolete and troublesome ones, to provide technologically-advanced replacements.</p>
      <p>The key to the company's success is the maintenance of a close working relationship with the clients. This is accomplished by ensuring the best possible solutions for their needs in order to establish and maintain a thorough knowledge and understanding of clients' objectives, helping maximize the benefits.</p>
      <p>We at Raslan Valveworks are a group of enthusiastic professionals who take pride in providing quality products to our clients. We help them find the best solutions for their needs by providing highly-experienced consultation services.</p>
    </div>
    <h3 class="section-head" style="left:58px; top:354px;">Company Values</h3>
    <div class="head-bar" style="left:262px; top:361px; width:221px;"></div>
    <p class="body-text on-white" style="left:58px; top:389px; width:368px; text-align:left;">At Raslan Valveworks, we are committed to providing the best solutions to our clients and improving our skill sets and technology to deliver high-quality valves and valve components.</p>
    <h3 class="section-head" style="left:58px; top:446px;">Our Vision</h3>
    <div class="head-bar" style="left:188px; top:452px; width:295px;"></div>
    <p class="body-text on-white" style="left:58px; top:481px; width:368px; text-align:left;">To become the most trusted valve advisor in the region, maintaining the integrity and reliability of our services among our clients.</p>
    <h3 class="section-head" style="left:58px; top:525px;">Our Mission</h3>
    <div class="head-bar" style="left:208px; top:531px; width:275px;"></div>
    <p class="body-text on-white" style="left:58px; top:560px; width:368px;">To cooperate with our clients in finding the most reliable and cost-effective solutions for their valve-related requirements.</p>
  </section>

  <!-- Inner 2 -->
  <section class="panel fill-grey" style="left:565px; top:900px; width:482px; height:682px;">
    <h2 class="title" style="left:87px; top:71px;">Strategic Approach</h2>
    <div class="body-text" style="left:87px; top:106px; width:210px; font-size:9.9px; line-height:12.4px;">
      <p>The most important aspect of the solutions provided by us is that we deliver tailor-fit designs to accurately and effectively meet the needs that are not well-served by the valves currently available in the market. As in current valve manufacturing companies, the engineers are limited to providing standard designs created by their companies. This also limits them from fulfilling any type of modification requirement. For this reason, there are many valve problems that cannot be solved by standard designs. Furthermore, the parts replacements provided by us meet the requirements and come at a much lower cost, as compared to the parts delivered by these manufacturers.</p>
      <p style="margin-top:12.4px;">We are open and cooperate with several trusted companies to find the best solutions for the end-user problems by providing detailed analysis and consultation services, helping them to buy the most relevant products as per their needs. We aim to be the best choice in valve consultation.</p>
    </div>
    <div class="abs fill-orange" style="left:0; top:420px; width:424px; height:262px;"></div>
    <h2 class="title" style="left:87px; top:428px;">Our Solutions</h2>
    <p class="body-text" style="left:87px; top:464px; width:210px; font-size:9.9px; line-height:12.4px;">Raslan Valveworks offers a full range of consultation services to help analyze your plant requirements for the effective implementation of solutions from our range of products. We cooperate with the end-user for a detailed analysis of the root cause and provide reliable solutions for different kinds of valve problems. Our products and services could be briefly divided into the following sections:</p>
  </section>

  <!-- Inner 3 -->
  <section class="panel fill-white" style="left:1047px; top:900px; width:481px; height:682px;">
    <div class="photo" role="img" aria-label="3D cut-away render of a valve body with blue trim and stacked disc cage" style="left:0; top:0; width:481px; height:332px; background:linear-gradient(135deg,#3A3D40 0%,#9A9EA2 35%,#6C8BA8 55%,#B4B8BC 75%,#4C5054 100%);"></div>
    <p class="body-text" style="left:57px; top:430px; width:314px; color:var(--text-grey);">We provide consultation on and design of a variety of valves for different kinds of industrial applications. We have a rich set of valve designs and solutions available, providing solutions for severe service applications. For special valve solutions not available in the market, we can help our clients by manufacturing and delivering those valves in the shortest possible timeframe under the most complicated requirements</p>
  </section>

  <div class="abs fill-orange" style="left:989px; top:1232px; width:539px; height:88px;"></div>
  <h2 class="title" style="left:1104px; top:1290px;">New Valves</h2>
  <div class="abs fill-grey" style="left:989px; top:1320px; width:58px; height:262px;"></div>

  <!-- Inner 4 -->
  <section class="panel" style="left:1528px; top:900px; width:482px; height:682px;">
    <div class="photo" role="img" aria-label="Control valve with red actuator and grey globe body standing on a pallet in a workshop" style="left:0; top:0; width:482px; height:682px; background:linear-gradient(180deg,#D7D2CA 0%,#C9543A 12%,#B84A32 30%,#8E9193 42%,#535B5E 60%,#4A5255 85%,#B89A74 100%);"></div>
  </section>

  <div class="spread-frame" style="left:82px; top:900px; width:1928px; height:682px;"></div>

  <span class="page-label" style="left:95px; top:1592px;">inner 1</span>
  <span class="page-label" style="left:577px; top:1592px;">inner 2</span>
  <span class="page-label" style="left:1064px; top:1592px;">inner 3</span>
  <span class="page-label" style="left:1543px; top:1592px;">inner 4</span>

</div>
</body>
</html>
```